Optical ad for newspaper

I attached an old ad. I want a totally NEW look with most of the same information.

The changes to the offer are:
1. Heading: FINAL LIQUIDATION
of designer eyewear
2. Changes in the offers: 40-75 becomes 50-80
3. Exp date: 09-26-15
4. 2 Sizes needed: 10" x 10"
6.5" x 10"

```html
<!DOCTYPE html>
<html lang="en">
<head>
<meta charset="utf-8">
<title>Final Liquidation – Lakeside Opticians</title>
<link rel="stylesheet" href="https://fonts.googleapis.com/css2?family=Oswald:wght@500;700&family=Open+Sans:wght@400;600;700;800&family=Lobster&display=swap">
<style>
  :root{
    --frame:#8a5a32;
    --frame-dark:#6e4424;
    --paper:#ffffff;
    --blue:#1f4fa8;
    --red:#e0262d;
    --ink:#2b2b2b;
    --photo-a:#d9b79a;
    --photo-b:#6b4a36;
  }
  *{box-sizing:border-box;margin:0;padding:0}
  html,body{width:805px;height:1200px;overflow:hidden}
  body{background:linear-gradient(135deg,var(--frame),var(--frame-dark));font-family:"Open Sans",Arial,sans-serif;color:var(--ink)}
  .ad{position:absolute;left:22px;top:22px;width:761px;height:1156px;background:var(--paper);overflow:hidden}

  .headline{position:absolute;left:22px;top:14px;z-index:3}
  .headline .lead{font-family:"Lobster",cursive;color:var(--blue);font-size:32px;line-height:1}
  .headline .main{font-family:"Oswald",Arial,sans-serif;font-weight:700;color:var(--blue);font-size:52px;line-height:1.05;letter-spacing:1px}
  .headline .sub{display:inline-block;margin-top:2px;background:var(--red);color:#fff;font-weight:700;font-size:15px;padding:3px 12px;letter-spacing:1px}

  .photo{position:absolute;left:0;top:150px;width:610px;height:750px;z-index:1;background:radial-gradient(ellipse at 40% 35%,var(--photo-a) 0%,#b8876a 45%,var(--photo-b) 100%)}

  .bubble{position:absolute;left:370px;top:40px;width:385px;height:280px;z-index:2}
  .bubble svg{position:absolute;inset:0}
  .bubble .copy{position:absolute;left:78px;top:56px;width:290px;color:#fff}
  .bubble .pct{font-family:"Oswald",Arial,sans-serif;font-weight:500;font-size:48px;line-height:1;white-space:nowrap}
  .bubble .off{font-weight:800;font-size:19px;margin-top:10px}
  .bubble .note{font-size:14px;line-height:1.35;font-weight:600}

  .extras{position:absolute;right:16px;top:470px;width:130px;text-align:right;z-index:2}
  .extra .plus{font-weight:700;font-size:16px}
  .extra .what{font-weight:600;font-size:12px;line-height:1.2}
  .extra .fine{font-size:9px;line-height:1.2}
  .or{font-weight:700;font-size:16px;margin:10px 0;padding-top:6px;border-top:1px solid #999}

  .combine{position:absolute;left:0;top:905px;width:761px;height:56px;background:var(--red);color:#fff;font-family:"Oswald",Arial,sans-serif;font-weight:700;font-size:32px;display:flex;align-items:center;justify-content:center;letter-spacing:1px}

  .brand{position:absolute;left:20px;top:1010px;width:210px;display:flex;flex-direction:column;align-items:center;gap:10px}
  .brand .dot{width:64px;height:64px;border-radius:50%;background:var(--red)}
  .brand .name{font-weight:800;color:var(--red);font-size:17px;letter-spacing:1px;white-space:nowrap}

  .expiry{position:absolute;right:20px;top:976px;font-size:14px;font-weight:600}
  .contact{position:absolute;left:300px;top:1005px;width:445px}
  .contact .phone{color:var(--blue);font-weight:800;font-size:28px;line-height:1.1;white-space:nowrap}
  .contact .hours{color:var(--red);font-weight:700;font-size:18px;margin-top:4px;white-space:nowrap}
  .contact .where{font-size:13px;margin-top:6px;font-weight:600;line-height:1.4}
  .contact .where b{color:var(--blue)}
</style>
</head>
<body>
<main class="ad">
  <div class="photo" role="img" aria-label="Photo of a smiling woman wearing designer eyeglasses"></div>

  <header class="headline">
    <div class="lead">Final</div>
    <div class="main">LIQUIDATION</div>
    <div class="sub">OF DESIGNER EYEWEAR</div>
  </header>

  <section class="bubble">
    <svg viewBox="0 0 385 280" width="385" height="280" aria-hidden="true">
      <defs>
        <radialGradient id="sky" cx="40%" cy="35%" r="70%">
          <stop offset="0" stop-color="#4fb0f5"/>
          <stop offset="1" stop-color="#1565c0"/>
        </radialGradient>
      </defs>
      <path d="M60 30 Q190 -10 340 15 Q390 60 375 150 Q380 245 280 268 Q150 292 60 245 Q0 200 20 115 Q22 55 60 30 Z" fill="url(#sky)"/>
    </svg>
    <div class="copy">
      <div class="pct">50 % - 80 %*</div>
      <div class="off">Off Non- RX Sunglasses</div>
      <div class="note">grab n go or put your rx in<br>them to save more!<br>Certain Names Excluded.</div>
    </div>
  </section>

  <aside class="extras">
    <div class="extra">
      <div class="plus">*Plus</div>
      <div class="what">Free Second pair</div>
      <div class="fine">with any complete pair purchase</div>
    </div>
    <div class="or">OR</div>
    <div class="extra">
      <div class="plus">*Plus</div>
      <div class="what">Free Non-RX Sunglass</div>
      <div class="fine">Many to chose from</div>
    </div>
    <div class="or">OR</div>
    <div class="extra">
      <div class="plus">*Plus</div>
      <div class="what">Ready made Readers</div>
      <div class="fine">Many to choose from</div>
    </div>
  </aside>

  <div class="combine">FRIENDS &amp; FAMILY CAN COMBINE!</div>

  <div class="brand">
    <span class="dot"></span>
    <span class="name">LAKESIDE OPTICIANS</span>
  </div>

  <div class="expiry">Offer Exp: 09-26-15</div>

  <section class="contact">
    <div class="phone">Contact Us 555-014-2278</div>
    <div class="hours">Open Mon.-Wed. 10-6 | Thurs. - Sat. 10-9</div>
    <div class="where">Shop At Harbor Center on Palm Road | <b>LAKESIDEOPTICIANS.COM</b><br>(Next to Pepe's Cantina and Golden Lotus)</div>
  </section>
</main>
</body>
</html>
```